Business Card Design and Logo Needed

I need Business Cards and a Logo for my website and public speaking business which can be found at: www.kelsa-thorn.example

I'm looking for creative and unique ideas. Some business cards I've found online that I like can be found at:
http://gigplatelo.example/general/18-smokin-hot-business-card-designs/

and at

http://www.vortaplume.example/2009/04/50-creative-business-cards-of-50-graphic-designers/

```html
<!DOCTYPE html>
<html lang="en">
<head>
<meta charset="utf-8">
<title>Kelsa Thorn — Business Card</title>
<link rel="stylesheet" href="https://fonts.googleapis.com/css2?family=Questrial&display=swap">
<style>
  :root {
    --paper-light: #ffffff;
    --paper-mid: #e4e4e4;
    --paper-edge: #8a8a8a;
    --ink: #0a0a0a;
    --band-dark: #262626;
    --band-black: #050505;
    --name-tone: #d9d9d9;
    --role-tone: #5b5b5b;
    --url-tone: #f2f2f2;
  }
  * { margin: 0; padding: 0; box-sizing: border-box; }
  html, body {
    width: 1200px;
    height: 720px;
    overflow: hidden;
    background: var(--band-dark);
  }
  .card {
    position: relative;
    width: 1200px;
    height: 720px;
    font-family: "Questrial", "Century Gothic", sans-serif;
    overflow: hidden;
  }
  .card__top {
    position: absolute;
    left: 0; top: 0;
    width: 1200px; height: 352px;
    background:
      radial-gradient(ellipse 75% 95% at 50% 45%, var(--paper-light) 0%, var(--paper-mid) 55%, var(--paper-edge) 100%);
  }
  .brand-mark {
    position: absolute;
    left: 50%; top: 150px;
    transform: translateX(-50%);
    display: flex;
    align-items: center;
    gap: 18px;
    color: var(--ink);
    font-size: 40px;
    letter-spacing: 2px;
    white-space: nowrap;
  }
  .brand-mark__dot {
    width: 34px; height: 34px;
    border-radius: 50%;
    background: var(--ink);
  }
  .card__bottom {
    position: absolute;
    left: 0; top: 352px;
    width: 1200px; height: 368px;
    background: var(--band-dark);
    box-shadow: 0 -6px 10px rgba(0,0,0,0.55);
  }
  .card__bottom svg {
    position: absolute; left: 0; top: 0;
  }
  .site-url {
    font-family: "Questrial", "Century Gothic", sans-serif;
    font-size: 32px;
  }
  .name {
    position: absolute;
    left: 363px; top: 55px;
    font-size: 66px;
    font-weight: 400;
    letter-spacing: 3px;
    color: var(--name-tone);
    text-shadow: 3px 3px 4px rgba(0,0,0,0.8);
    white-space: nowrap;
  }
  .roles {
    list-style: none;
    position: absolute;
    left: 0; top: 163px;
    color: var(--role-tone);
    font-size: 36px;
    line-height: 44px;
    letter-spacing: 1px;
    white-space: nowrap;
  }
  .roles li:nth-child(1) { padding-left: 325px; }
  .roles li:nth-child(2) { padding-left: 387px; }
  .roles li:nth-child(3) { padding-left: 503px; }
</style>
</head>
<body>
<main class="card">
  <section class="card__top">
    <div class="brand-mark">
      <span class="brand-mark__dot"></span>
      <span class="brand-mark__name">Kelsa Thorn</span>
    </div>
  </section>

  <section class="card__bottom">
    <svg width="1200" height="368" viewBox="0 0 1200 368">
      <polygon class="url-strip" points="0,0 203,0 336,368 0,368" fill="var(--band-black)"/>
      <text class="site-url" x="0" y="0" fill="var(--url-tone)" textLength="330" lengthAdjust="spacingAndGlyphs" transform="translate(142 28) rotate(67)">Kelsa-Thorn.example</text>
    </svg>
    <h1 class="name">KELSA THORN</h1>
    <ul class="roles">
      <li>SPEAKER</li>
      <li>PHILANTHROPIST</li>
      <li>AND AUTHOR OF UPCOMING BOOK</li>
    </ul>
  </section>
</main>
</body>
</html>
```